Vocational Mentor needs an impressive business card

1. I need a business card (or maybe three with identic look) to promote me and my three business titles/services:
- Vocational Mentor. I help people find their vocation and live happily from it. I use my 20 years of experience in business, management and psychology to help them identify the most efficient ways to make a living doing what they are passionate about.
- Business Angel. I help founders start a succesful business with minimum risks and costs. I use my 20 years of experience in sales, management and entrepreneurship to help them identify the most efficient ways, in terms of time and cost, to validate their business idea.
- Learning Designer. I design unique learning programs that produce long-term cognitive and behavioural changes to people and organisations. I use my 20 years of experience in learning, teaching and change management to create minimalist experiences and processes that allow them to change efficiently in their pursued direction.

2. I would like a two-sided business card, on the front with my name, contact details and titles, on the back the explanation of the services.
Updates

Hi all,

I updated my brief, included contacts info and give feedback on all designs I got. I am new on this platform so please tell me if you need anything else or if I don't use corectly the platform forms.

Kind regards,
Mirel

Hi all,

I shortened the services description by deleting the phrase "I call..."

Kind regards,
Mirel

Target Market(s)

Freelancers, startups, people and organization willing to invest in change through ultimate learning experiences

Industry/Entity Type

Business

Font styles to use
Serif

Requirements
Must have
• Front side: full name, titles, web site, email, phone like below:
Mirel Vantaru
Vocational Mentor, Business Angel, Learning Designer
info@mirelvantaru.example
www.mirelvantaru.example
+40-748-MIRELV
Nice to have
• Back side: the description of the services I provide as in the task description.
1/3: it would be nice if I can jam all three titles on the front side but then I need a solution to jam all three services on the back side.

```html
<!DOCTYPE html>
<html lang="en">
<head>
<meta charset="utf-8">
<title>Mirel Vantaru – Business Card</title>
<link href="https://fonts.googleapis.com/css2?family=Lato:wght@300;400;700;900&display=swap" rel="stylesheet">
<style>
  :root {
    --backdrop: #1f1f21;
    --card: #ffffff;
    --brand-red: #a51d2d;
    --brand-red-dark: #7d1421;
    --ink: #1e1e1e;
    --white: #ffffff;
  }
  * { box-sizing: border-box; margin: 0; padding: 0; }
  html, body {
    width: 1200px; height: 926px; overflow: hidden;
    background: var(--backdrop);
    font-family: "Lato", Arial, sans-serif;
    color: var(--ink);
  }
  .canvas { position: relative; width: 1200px; height: 926px; }

  .card {
    position: absolute; left: 240px;
    width: 720px; height: 411px;
    background: var(--card);
    overflow: hidden;
  }
  .card--front { top: 32px; }
  .card--back  { top: 483px; }

  /* Front */
  .name-accent {
    position: absolute; top: 150px; left: 232px;
    width: 14px; height: 40px;
    background: var(--brand-red);
    clip-path: polygon(55% 0, 100% 0, 45% 100%, 0 100%);
  }
  .name-band {
    position: absolute; top: 150px; left: 244px; right: 0;
    height: 40px;
    background: var(--brand-red);
    border-bottom: 4px solid var(--brand-red-dark);
    clip-path: polygon(22px 0, 100% 0, 100% 100%, 0 100%);
    color: var(--white);
    font-size: 27px; line-height: 37px;
    letter-spacing: 0.5px; text-transform: uppercase;
    padding-left: 30px;
  }
  .name-band .given { font-weight: 300; }
  .name-band .family { font-weight: 900; }
  .titles {
    position: absolute; top: 196px; left: 258px;
    font-size: 13.5px; font-weight: 900;
    text-transform: uppercase; letter-spacing: 0.2px;
  }
  .contacts {
    position: absolute; top: 250px; left: 250px;
    list-style: none;
  }
  .contacts li {
    display: flex; align-items: center;
    height: 27px; font-size: 17px;
  }
  .contact-key {
    width: 21px; height: 21px; margin-right: 14px;
    background: var(--brand-red); color: var(--white);
    font-size: 13px; font-weight: 700;
    display: flex; align-items: center; justify-content: center;
  }
  .contacts li:nth-child(1) .contact-key { margin-left: 14px; margin-right: 14px; }
  .contacts li:nth-child(2) .contact-key { margin-left: 7px;  margin-right: 21px; }
  .contacts li:nth-child(3) .contact-key { margin-left: 0;    margin-right: 28px; }
  .contacts li:nth-child(4) { padding-left: 49px; }
  .contact-phone { font-weight: 900; font-size: 18px; }

  /* Back */
  .services {
    position: absolute; inset: 18px 18px 0 18px;
    display: grid; grid-template-columns: repeat(3, 1fr); gap: 10px;
  }
  .service { position: relative; }
  .service-head {
    background: var(--brand-red); color: var(--white);
    height: 68px; padding: 10px 12px;
    font-size: 22px; line-height: 24px;
    text-transform: uppercase;
  }
  .service-head .light { display: block; font-weight: 300; }
  .service-head .bold  { display: block; font-weight: 900; }
  .service-text {
    padding: 12px 10px 0 10px;
    font-size: 14px; line-height: 18px;
  }
  .service-foot {
    position: absolute; left: 0; right: 0; bottom: 16px;
    height: 12px; background: var(--brand-red);
  }
</style>
</head>
<body>
<main class="canvas">

  <section class="card card--front" aria-label="Business card front">
    <div class="name-accent"></div>
    <h1 class="name-band"><span class="given">Mirel</span> <span class="family">Vantaru</span></h1>
    <p class="titles">Vocational Mentor, Business Angel, Learning Designer</p>
    <ul class="contacts">
      <li><span class="contact-key">P</span><span class="contact-phone">0400 555 019</span></li>
      <li><span class="contact-key">E</span><span>info@mirelvantaru.example</span></li>
      <li><span class="contact-key">W</span><span>www.mirelvantaru.example</span></li>
      <li><span>www.mirelvantaru.example</span></li>
    </ul>
  </section>

  <section class="card card--back" aria-label="Business card back">
    <div class="services">
      <article class="service">
        <h2 class="service-head"><span class="light">Vocational</span><span class="bold">Mentor</span></h2>
        <p class="service-text">I help people to find their vocation and live happily from it. I use my 20 years of experience in business, management and psychology to help them identify the most efficient ways to make a living doing what they are passionate about.</p>
        <div class="service-foot"></div>
      </article>
      <article class="service">
        <h2 class="service-head"><span class="light">Business</span><span class="bold">Angel</span></h2>
        <p class="service-text">I help founders to start a succesful business with minimum risks and costs. I use my 20 years of experience in sales, management and entrepreneurship to help them identify the most efficient ways, in terms of time and cost, to validate their business idea.</p>
        <div class="service-foot"></div>
      </article>
      <article class="service">
        <h2 class="service-head"><span class="light">Learning</span><span class="bold">Designer</span></h2>
        <p class="service-text">I design unique learning programs that produce long-term cognitive and behavioural changes to people and organisations. I use my 20 years of experience in learning, teaching and change management to create minimalist experiences and processes that allows them to change efficiently in their pursued direction.</p>
        <div class="service-foot"></div>
      </article>
    </div>
  </section>

</main>
</body>
</html>
```